Real Estate Marketing Flyer-8.5 by 11 Dual Sided

This is Direct Marketing Flyer targeted to Condo Property owners
to list their condos/townhomes with us. We are looking for Stylish graphics with more upscale design and colors to standout from other agents in the marketplace.

We are open to how it is presented or any design choices made that make flyer standout/appealing.

Target Market(s)

Condo Property Owners..and to lesser extent buyers

Industry/Entity Type

Real Estate

Requirements
Must have
• First Page

Top

Banner with our Team Pic and Names Priscilla, Lou and Bea
(Insert a background photo of condominium complex of upper scale)

"Specializing in Condos/Townhomes"

Buying* Selling* Leasing* Short Sales

1 866 4Suite4 (784-8324)

www.BayviewSuiteGroup.com

When It's time to Sell, Lease of Buy
Contact us for FREE No Obligation Market Consultation

Select Recent Sales By The Bayview Suite Group

7182 W Hollander Ct. # B (688,698)

3 Bedroom 2.5 Bathroom *Represented Buyer*

4217 W Larkfield St. #41
(006,0176)

2 Bedroom 2.5 Bathroom *Water View*

814 S. Marrowbrook-23 2 Bedroom,2.5 Bathroom

3316 W. Loma Tranquila 2 Bedroom 2 Bathroom

26743 Fern Hollow 4 Bedroom 3 Bathrooms

Leasing-We Do That Too

Complete Landlord/Tenant Services

7461 Juniper (54.28)

2 Bedroom, 2 Bathroom

4219 W.Larkfield-38 1 Bedroom, 1 Bathroom

8027 E. Corvallo-216 3 Bedroom, 2.5 Bathroom

937 S. Trellis -D 2 Bedroom 2.5 Bathroom

News You Can Use

Consumer confidence reached a five-year high in May, according to a Merrow Council report also released on Tuesday, with big improvements in Americans’ views about both the current economy and future economic conditions. Consumer spending has also been strikingly resilient so far this year

The Dunmore-Wick 20-city composite index rose 10.9 percent over the last year, the biggest increase since April 2006. Several cities — Charlotte, N.C.; Los Angeles; Portland, Ore.; Seattle; and Tampa, Fla. — had their largest month-over-month gains in more than seven years.

Have you installed Carbon Monoxide detectors in Your Property?

As of July 1, 2011 the Household Air Safety Standards Act (Senate Bill - SB 472) requires owners of all single-family homes with an attached garage or a fossil fuel source to install carbon monoxide detectors within the home by July 1, 2011. Owners of multi-family leased or rental dwellings, such as apartment buildings, have until January 1, 2013 to comply with the law

Home Loan Relief Measure extended through 2013-The BayviewSuiteGroup has extensive experience doing Short Sales-call us for free consultation on doing a No Cost Short Sale.

The best way to cheer yourself up is to try to cheer somebody else up.
Edwin Harlow

Picture of Cute Dog and Cute Bea

We love Pets..When you buy or sell with TheBayviewSuiteGroup-we will make a donation to the animal shelter of your choice.

email contacts

lou@bayviewsuitegroup.com
bea@bayviewsuitegroup.com
priscilla@bayviewsuitegroup.com

(in very small print)

if your property is currently listed with a broker, this is not intention as a solicitation

Nice to have
• We provide cutting edge marketing along with good old fashioned service and hard work

Our "Total Outreach" program offers an overwhelming array of advertising designed to sell your property for top dollar and find the perfect buyer.

We also Provide Free Complete Home Staging consultation, Innovative Value Range Pricing options and so much more.

```html
<!DOCTYPE html>
<html lang="en">
<head>
<meta charset="utf-8">
<title>The Bayview Suite Group – Condo Flyer</title>
<link href="https://fonts.googleapis.com/css2?family=Anton&family=PT+Serif:wght@400;700&display=swap" rel="stylesheet">
<style>
  :root {
    --blue: #0f6fb6;
    --orange: #ff6a00;
    --green: #a3c83b;
    --ink: #111111;
    --dark: #3a3a3a;
    --olive: #3d4a12;
    --white: #ffffff;
  }
  html, body { margin: 0; padding: 0; overflow: hidden; }
  body { width: 927px; height: 1200px; background: var(--blue); }
  .flyer {
    position: relative; width: 927px; height: 1200px; overflow: hidden;
    background: var(--blue); color: var(--white);
    font-family: "PT Serif", Georgia, serif;
  }
  .flyer > * { position: absolute; margin: 0; }
  .brand-square { left: 20px; top: 0; width: 114px; height: 146px; background: var(--orange); }
  .team-title { right: 48px; top: 44px; font-size: 42px; letter-spacing: 1px; font-weight: 400; white-space: nowrap; }
  .team-names { right: 48px; top: 103px; font-size: 34px; font-weight: 400; white-space: nowrap; }
  .tagline {
    left: 0; width: 927px; top: 158px; text-align: center;
    font-family: "Anton", Impact, sans-serif; font-size: 56px; color: var(--ink);
    letter-spacing: 0.5px; white-space: nowrap;
    text-shadow: 2px 0 0 #fff, -2px 0 0 #fff, 0 2px 0 #fff, 0 -2px 0 #fff,
                 2px 2px 0 #fff, -2px -2px 0 #fff, 2px -2px 0 #fff, -2px 2px 0 #fff;
  }
  .news-heading { left: 37px; top: 252px; font-size: 52px; font-weight: 400; }
  .photo-frame { width: 242px; height: 160px; }
  .photo-frame .back { position: absolute; inset: 0; background: var(--orange); transform: rotate(5deg); }
  .photo-frame .pic {
    position: absolute; inset: 0; border: 5px solid #fff; box-sizing: border-box;
    transform: rotate(-4deg); box-shadow: 0 2px 6px rgba(0,0,0,.35);
  }
  .news-photo { left: 33px; top: 318px; }
  .news-photo .pic { background: linear-gradient(160deg, #cfd6dc 0%, #e9ecee 45%, #8aa07a 100%); }
  .news-text { left: 322px; top: 258px; width: 560px; font-size: 16.2px; line-height: 21.8px; }
  .news-text p { margin: 0 0 21px; }
  .safety-band { left: 0; top: 508px; width: 927px; height: 171px; background: var(--orange); }
  .safety-heading { left: 30px; top: 518px; font-size: 25px; font-weight: 400; }
  .safety-text { left: 30px; top: 563px; width: 840px; font-size: 16px; line-height: 21.8px; }
  .relief-note { left: 29px; top: 698px; width: 890px; font-size: 20.5px; line-height: 29px; }
  .quote { right: 246px; top: 770px; text-align: right; color: var(--ink); font-size: 23px; line-height: 29px; }
  .quote cite { display: block; font-style: normal; font-size: 14px; line-height: 18px; }
  .pet-photo { left: 38px; top: 792px; }
  .pet-photo .pic { background: linear-gradient(180deg, #b9d5ea 0%, #7eb7d6 50%, #c9a46a 100%); }
  .pet-note { left: 41px; top: 976px; width: 260px; font-size: 15.8px; line-height: 22px; }
  .contact-circle { left: 378px; top: 851px; width: 290px; height: 290px; border-radius: 50%; background: var(--green); }
  .mail-icon { left: 485px; top: 876px; }
  .contact-heading { left: 368px; width: 300px; top: 908px; text-align: center; font-size: 31px; font-weight: 400; }
  .contact-list { left: 350px; width: 330px; top: 948px; text-align: center; color: var(--ink); font-size: 18px; line-height: 27px; list-style: none; padding: 0; }
  .team-photo { left: 660px; top: 839px; width: 253px; height: 250px; background: linear-gradient(180deg, rgba(30,40,60,0) 0%, #1c2434 45%, #0d1118 100%); border-radius: 120px 120px 0 0; z-index: 1; }
  .phone { left: 400px; top: 1036px; font-family: "Anton", Impact, sans-serif; font-size: 27px; white-space: nowrap; letter-spacing: 0.3px; z-index: 2; }
  .footer { left: 0; top: 1089px; width: 927px; height: 111px; background: var(--dark); }
  .site-url { left: 39px; top: 1118px; font-size: 22px; }
  .disclaimer { left: 39px; top: 1162px; font-size: 10.5px; }
  .footer-mark { left: 500px; top: 1128px; display: flex; align-items: center; gap: 10px; font-size: 26px; white-space: nowrap; }
  .footer-mark .dot { width: 36px; height: 36px; border-radius: 50%; background: var(--orange); }
</style>
</head>
<body>
<main class="flyer">
  <div class="brand-square"></div>
  <h1 class="team-title">THE BAYVIEW SUITE GROUP</h1>
  <h2 class="team-names">PRISCILLA, LOU AND BEA</h2>
  <p class="tagline">"SPECIALIZING IN CONDOS/TOWNHOMES"</p>

  <h2 class="news-heading">NEWS</h2>
  <div class="photo-frame news-photo">
    <div class="back"></div>
    <div class="pic" role="img" aria-label="Photo of a modern white townhome with a garage and a tree"></div>
  </div>
  <div class="news-text">
    <p>Consumer confidence reached a five-year high in May, according to a Merrow Council report also released on Tuesday, with big improvements in Americans’ views about both the current economy and future economic conditions. Consumer spending has also been strikingly resilient so far this year</p>
    <p>The Dunmore-Wick 20-city composite index rose 10.9 percent over the last year, the biggest increase since April 2006. Several cities — Charlotte, N.C.; Los Angeles; Portland, Ore.; Seattle; and Tampa, Fla. — had their largest month-over-month gains in more than seven years.</p>
  </div>

  <div class="safety-band"></div>
  <h3 class="safety-heading">Have you installed Carbon Monoxide detectors in Your Property?</h3>
  <p class="safety-text">As of July 1, 2011 the Household Air Safety Standards Act (Senate Bill - SB 472) requires owners of all single-family homes with an attached garage or a fossil fuel source to install carbon monoxide detectors within the home by July 1, 2011. Owners of multi-family leased or rental dwellings, such as apartment buildings, have until January 1, 2013 to comply with the law</p>

  <p class="relief-note">Home Loan Relief Measure extended through 2013-The BayviewSuiteGroup has extensive experience doing Short Sales-call us for free consultation on doing a No Cost Short Sale.</p>

  <blockquote class="quote">The best way to cheer yourself up<br>is to try to cheer somebody else up.<cite>Edwin Harlow</cite></blockquote>

  <div class="photo-frame pet-photo">
    <div class="back"></div>
    <div class="pic" role="img" aria-label="Photo of a puppy and a kitten beside a pool"></div>
  </div>
  <p class="pet-note">We love Pets..When you buy or sell with TheBayviewSuiteGroup-we will make a donation to the animal shelter of your choice.</p>

  <div class="contact-circle"></div>
  <svg class="mail-icon" width="58" height="32" viewBox="0 0 58 32" aria-hidden="true">
    <rect x="1" y="1" width="56" height="30" fill="var(--olive)"/>
    <polyline points="1,1 29,20 57,1" fill="none" stroke="var(--green)" stroke-width="2"/>
    <line x1="1" y1="31" x2="22" y2="15" stroke="var(--green)" stroke-width="2"/>
    <line x1="36" y1="15" x2="57" y2="31" stroke="var(--green)" stroke-width="2"/>
  </svg>
  <h3 class="contact-heading">email contacts</h3>
  <ul class="contact-list">
    <li>lou@bayviewsuitegroup.com</li>
    <li>bea@bayviewsuitegroup.com</li>
    <li>priscilla@bayviewsuitegroup.com</li>
  </ul>

  <div class="team-photo" role="img" aria-label="Photo of the three team members in business attire giving thumbs up"></div>
  <p class="phone">1 866 4SUITE4 (784-8324)</p>

  <footer class="footer"></footer>
  <p class="site-url">www.BayviewSuiteGroup.com</p>
  <p class="disclaimer">if your property is currently listed with a broker, this is not intention as a solicitation</p>
  <div class="footer-mark"><span class="dot"></span><span>THE BAYVIEW SUITE GROUP</span></div>
</main>
</body>
</html>
```